Business Card Design - Service Company

Use of the card mainly in living rooms and relations b2b We wish a card with a modern design, blue tones in the background would be a plus The card must be front / back (one side with the logo / the other with the information of contact )

Font styles to use
Serif

Requirements
Must have
• Using the map on the back of the business card Editable format! Photoshop CS2 / Illustrator CS2
Nice to have
• Maquis Forge IT Belvent Commercial Center, 20740 Orvenza 0495871432 Siret 48217390600128 APE 9623Y https://www.fb.com/studio.maquisforge www.maquis-forge.example

```html
<!DOCTYPE html>
<html lang="en">
<head>
<meta charset="utf-8">
<title>Maquis Forge IT – Business Card</title>
<link href="https://fonts.googleapis.com/css2?family=Lora:wght@400;600&display=swap" rel="stylesheet">
<style>
  :root {
    --stage: #1f2023;
    --card-grey: #6a6b6f;
    --card-grey-faint: #77787c;
    --card-white: #ffffff;
    --brand-blue: #2a88cc;
    --ink-grey: #5a5a5e;
    --rule-grey: #c9c9cc;
  }
  * { box-sizing: border-box; margin: 0; padding: 0; }
  html, body {
    width: 1200px; height: 800px; overflow: hidden;
    background: var(--stage);
    font-family: "Lora", Georgia, serif;
  }
  .canvas {
    width: 1200px; height: 800px;
    display: flex; align-items: center; justify-content: center; gap: 40px;
  }
  .card {
    position: relative;
    width: 560px; height: 320px;
    overflow: hidden;
    box-shadow: 0 18px 40px rgba(0,0,0,0.45);
  }

  /* Back side */
  .card-back { background: var(--card-grey); }
  .back-watermark {
    position: absolute; left: 28px; bottom: 26px;
    font-size: 62px; font-weight: 600; line-height: 1;
    color: var(--card-grey-faint);
    white-space: nowrap;
  }
  .back-name {
    position: absolute; right: 48px; top: 84px;
    display: flex; align-items: center; gap: 12px;
    color: var(--card-white);
    font-size: 30px; font-weight: 600;
  }
  .back-name .mark-square {
    width: 18px; height: 18px; background: var(--card-white);
  }

  /* Front side */
  .card-front { background: var(--card-white); }
  .front-name {
    position: absolute; left: 30px; top: 118px;
    display: flex; align-items: center; gap: 10px;
    color: var(--brand-blue);
    font-size: 23px; font-weight: 600;
    white-space: nowrap;
  }
  .front-name .mark-square {
    width: 14px; height: 14px; background: var(--brand-blue);
  }
  .divider {
    position: absolute; left: 264px; top: 58px;
    width: 1px; height: 150px; background: var(--brand-blue);
  }
  .contact {
    position: absolute; left: 284px; top: 58px;
    color: var(--ink-grey);
    font-size: 13px; line-height: 1.45;
  }
  .contact .company {
    color: var(--brand-blue); font-weight: 600;
    text-transform: uppercase; font-size: 13px;
  }
  .contact-list { list-style: none; margin-top: 10px; }
  .contact-list li { display: flex; align-items: center; gap: 7px; margin-bottom: 2px; }
  .contact-list svg { flex: none; }
  .band {
    position: absolute; left: 0; right: 0; top: 246px; height: 30px;
    background: var(--brand-blue);
    color: var(--card-white);
    font-size: 13px; line-height: 30px;
    padding-left: 80px;
  }
  .foot-rule {
    position: absolute; left: 0; right: 0; bottom: 12px; height: 2px;
    background: var(--rule-grey);
  }
</style>
</head>
<body>
<main class="canvas">
  <section class="card card-back" aria-label="Card back">
    <div class="back-watermark" aria-hidden="true">Maquis<br>Forge IT</div>
    <div class="back-name"><span class="mark-square"></span>Maquis Forge IT</div>
  </section>

  <section class="card card-front" aria-label="Card front">
    <div class="front-name"><span class="mark-square"></span>Maquis Forge IT</div>
    <div class="divider"></div>
    <div class="contact">
      <p class="company">Maquis Forge IT</p>
      <p>Belvent Commercial Center</p>
      <p>20740 Orvenza</p>
      <ul class="contact-list">
        <li>
          <svg width="13" height="13" viewBox="0 0 13 13" aria-hidden="true">
            <circle cx="6.5" cy="6.5" r="6" fill="none" stroke="#2a88cc" stroke-width="1.2"/>
            <path d="M4.3 3.6 L5.4 3.4 L6 5 L5.3 5.6 Q6 7.1 7.4 7.7 L8 7 L9.6 7.6 L9.4 8.7 Q6.9 9.2 5.2 7.6 Q3.8 6 4.3 3.6Z" fill="#2a88cc"/>
          </svg>
          0495871432
        </li>
        <li>
          <svg width="13" height="13" viewBox="0 0 13 13" aria-hidden="true">
            <circle cx="6.5" cy="6.5" r="6" fill="none" stroke="#2a88cc" stroke-width="1.2"/>
          </svg>
          studio.maquisforge
        </li>
        <li>
          <svg width="13" height="13" viewBox="0 0 13 13" aria-hidden="true">
            <circle cx="6.5" cy="6.5" r="6" fill="none" stroke="#2a88cc" stroke-width="1.2"/>
            <path d="M1 6.5 H12 M6.5 1 Q3.5 6.5 6.5 12 M6.5 1 Q9.5 6.5 6.5 12" fill="none" stroke="#2a88cc" stroke-width="0.8"/>
          </svg>
          www.maquis-forge.example
        </li>
      </ul>
    </div>
    <div class="band">Siret 48217390600128 APE 9623Y</div>
    <div class="foot-rule"></div>
  </section>
</main>
</body>
</html>
```